mobile offers/games platform requires email newsletter template

We send regular emails to consumers who have downloaded our mobile app and registered an account, as well as those that have expressed an interest but not yet registered (e.g. signed up for more information through facebook).

zestyOrbits is an exciting and innovative games platform which combines mobile gaming with offers to benefit both shoppers and retailers. Shoppers can play a range of fun mobile games – alone or together with their friends – and have their favourite brands give them great offers that help them succeed in the game. Top scorers win great prizes.

Our email newsletter is intended to alert consumers to :

* current competitions where they can win prizes using zestyOrbits
* current offers from retailers, which when taken up will give them a level up in the games and help them win prizes
* new retailers joining zestyOrbits
* new games launched within zestyOrbits
* other news from zestyOrbits - such as recent winners etc.

The majority of recipients open the email on smartPhones.

We would like a mobile friendly template that incorporates as standard links to :

* App Market and Play Shelf to download / update zestyOrbits
* offers on our website (zestyorbits.test)
* competitions on our website (zestyorbits.test)
* share on facebook with their friends about zestyOrbits
* forward the email to a friend
* follow us on twitter (twitter.com/zestyorbits)
* like us on facebook (facebook.com/zestyorbits)

and that gives us blocks that we can edit the content of each week to show :

* one or more current competitions
* one or more current offers
* other news (such as new retailers, new games, recent winners etc)

I have attached the zestyOrbits icon and a recent newsletter.

More information on zestyOrbits (the app) and 7quill (our company) can be found at :

www.zestyorbits.test
www.7quill.test
facebook.com/zestyorbits

We'd like the design to be really clean but with fun and innovation, and it must be good on mobile devices.

We currently use MailChimp and need the template to be fully coded load into that platform.

Thanks!

I forgot to say - on the footer we need include the following mandatory information, and an unubscribe link.

* copyright 7quill Pte Ltd 2013
* You are receiving this email because you expressed interest in, or are a player of, zestyOrbits.
* Our mailing address is:
7quill Pte Limited
41 Marlow Lane
Level 8 Velmora Tower
Singapore 072615

Target Market(s)

18-40 year old, currently all in Asia (mainly Singapore), males and females, enjoy mobile phone games, shopping, food and beverage, socialising and offers.

Industry/Entity Type

Games

Requirements
Must have
• Links to :
• * App Market and Play Shelf to download / update zestyOrbits
• * offers on our website (zestyorbits.test)
• * competitions on our website (zestyorbits.test)
• * share on facebook with their friends about zestyOrbits
• * forward the email to a friend
• * follow us on twitter (twitter.com/zestyorbits)
• * like us on facebook (facebook.com/zestyorbits)
• Blocks that we can edit the content of each week to show :
• * one or more current competitions
• * one or more current offers
• * other news (such as new retailers, new games, recent winners etc)
• Must be mobile friendly
• Must be coded for MailChimp

```html
<!DOCTYPE html>
<html lang="en">
<head>
<meta charset="utf-8">
<title>zestyOrbits Newsletter – November 2013</title>
<link rel="stylesheet" href="https://fonts.googleapis.com/css2?family=Nunito:wght@700;800&family=Open+Sans:wght@400;600;700&display=swap">
<style>
  :root {
    --topbar: #1a8ee0;
    --page: #f3f3f3;
    --card: #ffffff;
    --ink: #222222;
    --muted: #444444;
    --link: #2a78b4;
    --cyan: #22c9d8;
    --blue: #1a8fe0;
    --alert: #0b22d0;
    --rule: #b8b8b8;
    --footer: #dcdcdc;
    --badge: #111111;
    --badge-text: #ffffff;
  }
  * { box-sizing: border-box; margin: 0; padding: 0; }
  html, body { width: 768px; height: 1200px; overflow: hidden; }
  body {
    background: var(--page);
    font-family: "Open Sans", Arial, sans-serif;
    color: var(--ink);
    position: relative;
  }
  a { color: var(--link); text-decoration: none; }

  .topbar {
    height: 40px; background: var(--topbar); color: #fff;
    font-size: 9.5px; font-weight: 700; position: relative;
  }
  .topbar .notice { position: absolute; left: 73px; top: 12px; }
  .topbar .browser { position: absolute; left: 496px; top: 11px; line-height: 1.15; }
  .topbar .browser a { color: #fff; text-decoration: underline; }

  .masthead {
    position: absolute; left: 73px; top: 61px; width: 396px; height: 212px;
    background: linear-gradient(160deg, #1aa0e6 0%, #35c1d2 50%, #7ed67e 100%);
    color: #fff; text-align: center;
  }
  .brand {
    display: flex; align-items: center; justify-content: center; gap: 8px;
    margin-top: 64px; font-family: "Nunito", sans-serif; font-weight: 800;
    font-size: 30px; color: #0d4aa8;
  }
  .brand .mark { width: 18px; height: 18px; background: #0d4aa8; border-radius: 3px; }
  .tagline {
    margin-top: 48px; font-family: "Nunito", sans-serif; font-weight: 700;
    font-size: 14.5px; line-height: 1.08;
  }
  .issue-date {
    position: absolute; left: 490px; top: 158px;
    font-family: "Nunito", sans-serif; font-weight: 800; font-size: 15.5px; color: #333;
  }

  .main {
    position: absolute; left: 73px; top: 315px; width: 396px; height: 827px;
    background: var(--card); padding: 10px;
  }
  .hero {
    width: 376px; height: 250px;
    background: linear-gradient(180deg, #6f7a5c 0%, #a9a294 45%, #d9cbb4 75%, #8c8c86 100%);
  }
  .story { margin: 0 10px; padding: 20px 0 20px; border-bottom: 1px dotted var(--rule); }
  .story:last-child { border-bottom: 0; }
  .story h2 {
    font-family: "Nunito", sans-serif; font-weight: 800; font-size: 23.5px;
    line-height: 21px; color: var(--blue); margin-bottom: 12px; letter-spacing: 0.2px;
  }
  .story.feature h2 { color: var(--cyan); }
  .story p { font-size: 13.4px; line-height: 20.4px; color: var(--ink); letter-spacing: 0.25px; }
  .thumb { float: left; width: 88px; height: 88px; margin: 2px 4px 4px 4px; }
  .thumb.gems { background: linear-gradient(135deg, #2b1a3a, #7a2a6e 50%, #1e5c2a); }
  .thumb.walk { height: 56px; width: 90px; background: linear-gradient(180deg, #5a7a48, #8c9a6c 60%, #6c6a58); }

  .sidebar { position: absolute; left: 490px; top: 302px; width: 208px; }
  .sidebar h3 {
    font-family: "Nunito", sans-serif; font-weight: 800; font-size: 15.5px; color: #333;
  }
  .sidebar h3.alert { color: var(--alert); }
  .miss-list { list-style: none; margin-top: 7px; font-size: 12.5px; line-height: 19px; color: var(--muted); }
  .miss-list li::before { content: "• "; }
  .share { margin-top: 17px; font-size: 12.5px; }
  .store-badge {
    display: flex; align-items: center; gap: 8px;
    width: 130px; height: 41px; background: var(--badge);
    border-radius: 6px; margin-top: 2px; padding: 0 10px;
    color: var(--badge-text); font-family: "Open Sans", Arial, sans-serif;
    font-weight: 600;
  }
  .store-badge:first-of-type { margin-top: 3px; }
  .store-badge .dot { width: 14px; height: 14px; border-radius: 50%; background: var(--badge-text); flex: none; }
  .store-badge .label { display: flex; flex-direction: column; line-height: 1.05; }
  .store-badge .small { font-size: 8px; }
  .store-badge .big { font-size: 15px; }

  .offer { margin-top: 41px; font-size: 12.5px; line-height: 19px; color: var(--muted); }
  .offer .offer-img {
    float: left; width: 110px; height: 108px; margin-right: 2px;
    background: linear-gradient(180deg, #e9efe2, #9bc46a 55%, #5e8a3a);
  }
  .offer h4 {
    font-family: "Nunito", sans-serif; font-weight: 800; font-size: 19.5px;
    line-height: 15px; color: var(--cyan); padding-top: 3px; margin-bottom: 10px;
    padding-right: 14px;
  }

  .follow { margin-top: 42px; }
  .follow ul { list-style: none; margin-top: 8px; border-top: 1px dotted var(--rule); }
  .follow li {
    border-bottom: 1px dotted var(--rule); padding: 5px 0 4px;
    font-size: 12.5px; display: flex; align-items: center; gap: 7px;
  }
  .follow .icon { width: 16px; height: 16px; background: #333; }

  .footer {
    position: absolute; left: 0; top: 1163px; width: 768px; height: 37px;
    background: var(--footer); font-size: 11.5px; font-style: italic; color: #444;
  }
  .footer .copyright { position: absolute; left: 73px; top: 20px; }
  .footer .merge { position: absolute; left: 498px; top: 20px; font-style: normal; }
</style>
</head>
<body>
  <header class="topbar">
    <span class="notice">Don't miss the fun on our Friendbook Photo Contest! See the entries today!</span>
    <span class="browser">Is this email not displaying correctly?<br><a href="#">View it in your browser</a>.</span>
  </header>

  <section class="masthead">
    <div class="brand"><span class="mark"></span>zestyOrbits</div>
    <p class="tagline">Single and Multi-Player Mobile Games<br>with Real World Rewards</p>
  </section>
  <p class="issue-date">November 2013</p>

  <main class="main">
    <div class="hero" role="img" aria-label="Players dancing outdoors with a cartoon game character in the photo contest"></div>

    <article class="story feature">
      <h2>Dance Moves in our Photo Contest</h2>
      <p>jdfao noaise niasn dliaj .ansdi alnio enfa,s ch asb dfloua ablu sif ba, skudf b ais, dfbas fdasb m ansod in a,ksdfho aw, e jb akcja eor i ansdf. ser;oin ion difas</p>
    </article>

    <article class="story">
      <h2>Diamond Contest</h2>
      <div class="thumb gems" role="img" aria-label="Colourful gem puzzle game board"></div>
      <p>and thwi o htwo naodn foi ndf iafsdf as asdf adiae ionasiod went tow oaint on waot snf oias dfan&nbsp; soidnf iasdf asdfand thwi o htwo naodn foi ndf iafsdf as asdf adiae ionasiod went tow oaint on waot snf oias dfan&nbsp; soidnf iasdf asdf</p>
    </article>

    <article class="story">
      <h2>Fun Walk Through</h2>
      <div class="thumb walk" role="img" aria-label="Park path with trees during the fun walk"></div>
      <p>and thwi o htwo naodn foi ndf iafsdf as asdf adiae ionasiod went tow oaint on waot snf oias dfan&nbsp; soidnf iasdf asdfand thwi o htwo naodn foi ndf iafsdf as asdf adiae ionasiod went tow oaint on waot snf oias dfan&nbsp; soidnf iasdf asdf</p>
    </article>
  </main>

  <aside class="sidebar">
    <h3 class="alert">Don't Miss Out!</h3>
    <ul class="miss-list">
      <li><a href="#">Diamond Contest</a></li>
      <li>Fun Walk Through</li>
    </ul>

    <p class="share"><a href="#">Share with Friends</a></p>
    <a class="store-badge" href="#">
      <span class="dot"></span>
      <span class="label"><span class="small">Available on the</span><span class="big">App Market</span></span>
    </a>
    <a class="store-badge" href="#">
      <span class="dot"></span>
      <span class="label"><span class="small">Get it on</span><span class="big">Play Shelf</span></span>
    </a>

    <div class="offer">
      <div class="offer-img" role="img" aria-label="Iced green tea drinks and desserts"></div>
      <h4>Buy 1 Get One Free at Mellow Kyoto</h4>
      <p>Playing with friends is even more fun when you can share rewards. noin in oieh nsoierh ansiahsd foie nijno nlil nihnloun joinlgiu nion non kion o;</p>
    </div>

    <div class="follow">
      <h3>Keep Up With Us</h3>
      <ul>
        <li><span class="icon"></span><a href="#">Friendbook</a></li>
        <li><span class="icon"></span><a href="#">Chirper</a></li>
      </ul>
    </div>
  </aside>

  <footer class="footer">
    <span class="copyright">Copyright © *|CURRENT_YEAR|* *|LIST:COMPANY|*, All rights</span>
    <span class="merge">*|IF:REWARDS|*</span>
  </footer>
</body>
</html>
```